Venmora Crest Holdings Limited is a asset management company and project funding company, we specialise in high end finance for high net worth individuals, we are looking for a new logo letterhead template, email footer template and business card design. The letterhead template should be designed in word format so that the letterheading can be used electronically.

Below is the current logo that is a but plain and a little cheaper looking, colour schemes are not important just that it looks professional.

I am looking for a sharp impact that stands out,

Target Market(s)

High net worth individuals and institutions

Industry/Entity Type

Finance

Contact Information for Business Card

Venmora Crest Holdings Limited
T: 0333 418 2965

M: 07531 492718
E:derek.holt@venmora-cresthold.example

MARLOW QUAY, EAST CORAL ROAD
SECOND FLOOR, SUITE 210
P.O. BOX FX-47315
NASSAU BAHAMAS

Logo Text

Font styles to use
Serif
Sans Serif
Script
Other font styles liked:
• Tahoma

Colors
fbed22
6b449b
ec1f27
f78f20
33b8a4
0592cd

Requirements
Must have
• Colours schemes would look good in blue’s green’s purples.

Yellow and Purple together maybe a nice combination.
Nice to have
• I want the log to look sharpe, relate to a global presence, but I also want to it to look established.
Should not have
• N/a

```html
<!DOCTYPE html>
<html lang="en">
<head>
<meta charset="utf-8">
<title>Venmora Crest Holdings Limited – Stationery Set</title>
<link rel="stylesheet" href="https://fonts.googleapis.com/css2?family=Roboto:wght@400&family=Arimo:wght@400&display=swap">
<style>
  :root {
    --ink-navy: #021c22;
    --brand-blue: #00a0dc;
    --brand-teal: #005a7a;
    --mark-grey: #808285;
    --paper: #ffffff;
    --edge: #c8c8c8;
    --faint-blue: #e3f3fa;
    --faint-text: #d6e9f0;
    --black: #000000;
  }
  html, body {
    margin: 0;
    padding: 0;
    width: 1200px;
    height: 1200px;
    overflow: hidden;
    background: var(--paper);
  }
  .stationery-set { display: block; width: 1200px; height: 1200px; }
  .tagline { font-family: "Roboto", sans-serif; fill: var(--brand-teal); }
  .brand-name { font-family: "Arimo", sans-serif; fill: var(--brand-teal); }
  .sheet { fill: var(--paper); stroke: var(--edge); stroke-width: 2; }
  .band-dark { fill: var(--ink-navy); }
  .band-blue { fill: var(--brand-blue); }
  .band-teal { fill: var(--brand-teal); }
  .band-black { fill: var(--black); }
  .rule-blue { fill: none; stroke: var(--brand-blue); stroke-width: 4; }
  .brand-dot { fill: var(--brand-blue); }
  .watermark-dot { fill: var(--faint-blue); }
  .watermark-name { font-family: "Arimo", sans-serif; fill: var(--faint-text); }
  .small-white { font-family: "Arimo", sans-serif; fill: #ffffff; }
  .small-dark { font-family: "Arimo", sans-serif; fill: var(--ink-navy); }
  .card-text { font-family: "Arimo", sans-serif; fill: #ffffff; }
  .icon { fill: #ffffff; }
</style>
</head>
<body>
<svg class="stationery-set" viewBox="0 0 1920 1920" xmlns="http://www.w3.org/2000/svg">

  <!-- Identity panel -->
  <g class="identity">
    <circle class="brand-dot" cx="434" cy="490" r="175"/>
    <text class="brand-name" x="434" y="725" font-size="44" text-anchor="middle">Venmora Crest Holdings Limited</text>
    <text class="tagline" x="83" y="832" font-size="80">Omnia nos ducunt ad</text>
  </g>

  <!-- Letterhead -->
  <g class="letterhead">
    <rect class="sheet" x="1018" y="89" width="672" height="950"/>
    <polygon class="band-dark" points="1018,89 1548,89 1493,151 1018,151"/>
    <polygon class="band-dark" points="1018,151 1078,151 1056,174 1018,174"/>
    <polygon class="band-blue" points="1056,174 1074,154 1090,154 1072,174"/>
    <polygon class="band-blue" points="1082,174 1100,154 1112,154 1094,174"/>
    <polygon class="band-blue" points="1548,89 1690,89 1690,100 1660,100 1628,134 1508,134"/>
    <polyline class="rule-blue" points="1503,142 1636,142 1667,108 1690,108"/>

    <circle class="brand-dot" cx="1075" cy="119" r="22"/>
    <text class="small-white" x="1114" y="116" font-size="12.5">Venmora Crest</text>
    <text class="small-white" x="1114" y="132" font-size="12.5">Holdings Limited</text>

    <text class="small-white" font-size="9.5">
      <tspan x="1394" y="104">Marlow Quay East Coral Road</tspan>
      <tspan x="1394" y="116">Second Floor, Suite 210</tspan>
      <tspan x="1394" y="128">P.O. Box FX-47315</tspan>
      <tspan x="1394" y="140">Nassau Bahamas</tspan>
    </text>

    <circle class="watermark-dot" cx="1366" cy="541" r="118"/>
    <text class="watermark-name" x="1366" y="700" font-size="22" text-anchor="middle">Venmora Crest Holdings Limited</text>

    <polygon class="band-blue" points="1410,1012 1690,1012 1690,1039 1432,1039 1470,1017 1400,1017"/>
    <polygon class="band-dark" points="1018,1017 1472,1017 1432,1039 1018,1039"/>
    <text class="small-white" x="1026" y="1031" font-size="9.5">Tel: 0333 418 2965</text>
    <text class="small-dark" x="1675" y="1031" font-size="9.5" text-anchor="end">Company No. 482917C</text>
  </g>

  <!-- Business card front -->
  <g class="card-front">
    <rect class="sheet" x="31" y="1226" width="840" height="479"/>
    <circle class="brand-dot" cx="452" cy="1405" r="68"/>
    <text class="brand-name" x="452" y="1511" font-size="36" text-anchor="middle">Venmora Crest Holdings Limited</text>
    <path class="band-blue" d="M31,1595 C180,1655 420,1640 600,1595 C720,1568 800,1565 871,1578 L871,1705 L31,1705 Z"/>
    <path class="band-teal" d="M31,1595 C180,1665 440,1650 620,1618 C740,1598 810,1600 871,1612 L871,1705 L31,1705 Z"/>
    <path class="band-dark" d="M31,1595 C180,1672 460,1662 640,1632 C760,1612 830,1625 871,1650 L871,1705 L31,1705 Z"/>
    <text class="card-text" x="408" y="1687" font-size="20" text-anchor="middle">Tel: 0333 418 2965</text>
  </g>

  <!-- Business card back -->
  <g class="card-back">
    <rect class="sheet" x="1019" y="1226" width="840" height="479"/>
    <circle class="brand-dot" cx="1203" cy="1295" r="40"/>
    <text class="brand-name" x="1203" y="1357" font-size="21" text-anchor="middle">Venmora Crest Holdings Limited</text>
    <path class="band-blue" d="M1019,1360 C1150,1420 1350,1395 1500,1365 C1650,1333 1760,1325 1859,1345 L1859,1705 L1019,1705 Z"/>
    <path class="band-teal" d="M1019,1361 C1150,1425 1380,1405 1530,1380 C1680,1355 1780,1358 1859,1380 L1859,1705 L1019,1705 Z"/>
    <path class="band-black" d="M1019,1362 C1150,1430 1400,1415 1560,1393 C1700,1375 1790,1388 1859,1418 L1859,1705 L1019,1705 Z"/>

    <text class="card-text" x="1090" y="1552" font-size="48">Derek Holt</text>

    <path class="icon" d="M1446,1478 c-4,-6 -3,-14 2,-20 c5,-6 12,-9 18,-8 l4,6 l-6,5 l-4,-2 c-4,3 -6,8 -6,13 l4,2 l-2,7 z"/>
    <text class="card-text" x="1456" y="1534" font-size="30" text-anchor="middle">@</text>
    <polygon class="icon" points="1456,1562 1472,1577 1467,1577 1467,1589 1460,1589 1460,1581 1452,1581 1452,1589 1445,1589 1445,1577 1440,1577"/>

    <text class="card-text" font-size="21">
      <tspan x="1493" y="1481">07531 492718</tspan>
      <tspan x="1493" y="1604">Second Floor, Suite 210</tspan>
      <tspan x="1493" y="1578">Marlow Quay East Coral Road</tspan>
      <tspan x="1493" y="1630">P.O. Box FX-47315</tspan>
      <tspan x="1493" y="1656">Nassau Bahamas</tspan>
    </text>
    <text class="card-text" x="1493" y="1533" font-size="19" textLength="345" lengthAdjust="spacingAndGlyphs">derek.holt@venmora-cresthold.example</text>
  </g>
</svg>
</body>
</html>
```